Halvern Shipping

A flyer that sells both air and sea freight services. We had an attempt at this and wanted a fresh concept from your designers. Colors should be vibrant and the text readable on a digital billboard as well. Our attempt is attached along with our logo file.

Designers***The contents on our attempt flyer should be applied to your flyer design.

Thanks!

Industry/Entity Type

Shipping

```html
<!DOCTYPE html>
<html lang="en">
<head>
<meta charset="utf-8">
<title>Halvern Shipping – Flyer</title>
<link href="https://fonts.googleapis.com/css2?family=Montserrat:wght@600;700;800;900&family=Oswald:wght@600;700&display=swap" rel="stylesheet">
<style>
  :root{
    --red:#e32228;
    --blue:#2c5faf;
    --blue-deep:#1f4a93;
    --blue-light:#5b8fd0;
    --navy:#1c2c50;
    --tile-edge:#9bbbe8;
    --white:#ffffff;
    --stage:#e6e8eb;
  }
  *{margin:0;padding:0;box-sizing:border-box}
  html,body{width:1200px;height:3743px;overflow:hidden;background:var(--stage)}
  .flyer{position:absolute;left:39px;top:1089px;width:1123px;height:1565px;overflow:hidden;background:var(--white);font-family:"Montserrat",sans-serif}
  .backdrop{position:absolute;inset:0}
  .headline{position:absolute;left:40px;top:44px;color:var(--red);font-weight:900;font-size:88px;line-height:94px;letter-spacing:-1px}
  .headline-bar{position:absolute;left:0;top:56px;width:16px;height:160px;background:var(--red)}
  .logo-name{position:absolute;text-align:center;color:var(--red);font-weight:800;line-height:1.05}
  .logo-name--badge{left:510px;top:590px;width:200px;font-size:30px}
  .logo-name--footer{left:0;top:1405px;width:363px;font-size:38px}
  .offer-title{position:absolute;left:68px;top:790px;color:var(--white);font-family:"Oswald",sans-serif;font-weight:700;font-size:54px}
  .service{position:absolute;width:200px;text-align:center}
  .service-tile{width:174px;height:160px;margin:0 auto;border-radius:30px;background:var(--navy);border:4px solid var(--tile-edge);display:flex;align-items:center;justify-content:center}
  .service-art{width:112px;height:96px;border-radius:10px}
  .service-label{margin-top:8px;color:var(--white);font-family:"Oswald",sans-serif;font-weight:700;font-size:27px;letter-spacing:2px;line-height:28px}
  .footer-brand{position:absolute;left:0;top:1331px;width:363px;height:234px;background:var(--white)}
  .footer-info{position:absolute;left:363px;top:1331px;width:760px;height:217px;background:var(--blue-deep);color:var(--white);padding:22px 0 0 26px}
  .footer-strip{position:absolute;left:363px;top:1548px;width:760px;height:17px;background:var(--blue-light)}
  .cta{font-weight:700;font-size:34px;letter-spacing:1px}
  .contact{font-weight:700;font-size:23px;margin-top:4px;display:flex;align-items:center;gap:10px}
  .contact svg{flex:none}
  .phone{font-weight:800;font-size:50px;margin-top:6px}
  .social{position:absolute;right:28px;top:112px;display:flex;align-items:center;gap:10px;font-weight:700;font-size:22px}
  .social-dot{width:22px;height:22px;border-radius:50%;background:var(--white)}
</style>
</head>
<body>
<main class="flyer">
  <svg class="backdrop" width="1123" height="1565" viewBox="0 0 1123 1565">
    <defs>
      <linearGradient id="port" x1="0" y1="0" x2="1" y2="1">
        <stop offset="0" stop-color="#b9c7d6"/>
        <stop offset=".45" stop-color="#4c7bb0"/>
        <stop offset=".75" stop-color="#c0573f"/>
        <stop offset="1" stop-color="#2f4f7e"/>
      </linearGradient>
      <radialGradient id="transport" cx=".5" cy=".5" r=".6">
        <stop offset="0" stop-color="#3a66b6"/>
        <stop offset=".6" stop-color="#c9d3e2"/>
        <stop offset="1" stop-color="#f4f6f9"/>
      </radialGradient>
    </defs>
    <path d="M1123 110 C1000 260 880 450 540 745 L1123 745 Z" fill="#3a6cb8"/>
    <path d="M0 745 L560 745 C700 745 760 870 900 870 C1000 870 1080 810 1123 770 L1123 1565 L0 1565 Z" fill="var(--blue)"/>
    <path d="M560 745 C700 745 760 870 900 870 C1000 870 1080 810 1123 770 L1123 745 Z" fill="#6f9bd4"/>
    <g role="img" aria-label="Photo of a container port with cranes and stacked shipping containers">
      <rect x="0" y="208" width="600" height="440" fill="url(#port)"/>
    </g>
    <path d="M0 640 C200 700 420 690 600 630 L600 690 C420 760 200 770 0 720 Z" fill="var(--red)"/>
    <circle cx="833" cy="447" r="262" fill="var(--white)" stroke="var(--red)" stroke-width="16"/>
    <g role="img" aria-label="Illustration of a plane, cargo ship, globe, van and truck">
      <circle cx="833" cy="447" r="215" fill="url(#transport)"/>
    </g>
    <circle cx="610" cy="626" r="123" fill="var(--white)" stroke="var(--blue-light)" stroke-width="10"/>
  </svg>

  <div class="headline-bar"></div>
  <h1 class="headline">SAVE MONEY<br>SHIP BETTER!</h1>
  <div class="logo-name logo-name--badge">Halvern Shipping</div>

  <h2 class="offer-title">We Offer :</h2>

  <div class="service" style="left:141px;top:877px">
    <div class="service-tile"><div class="service-art" role="img" aria-label="Illustration of a hanging cargo container" style="background:#6fc99a"></div></div>
    <div class="service-label">CARGO</div>
  </div>
  <div class="service" style="left:461px;top:877px">
    <div class="service-tile"><div class="service-art" role="img" aria-label="Illustration of stacked parcels" style="background:linear-gradient(135deg,#e94b4b,#f2c84b)"></div></div>
    <div class="service-label">CONSOLIDATION</div>
  </div>
  <div class="service" style="left:773px;top:877px">
    <div class="service-tile"><div class="service-art" role="img" aria-label="Illustration of a plane among clouds" style="background:linear-gradient(135deg,#6fd2d6,#e4ecf2)"></div></div>
    <div class="service-label">AIR FREIGHT</div>
  </div>
  <div class="service" style="left:141px;top:1087px">
    <div class="service-tile"><div class="service-art" role="img" aria-label="Illustration of a cargo ship on waves" style="background:linear-gradient(180deg,#f0c04f,#38b7d4)"></div></div>
    <div class="service-label">SEA FREIGHT</div>
  </div>
  <div class="service" style="left:461px;top:1087px">
    <div class="service-tile"><div class="service-art" role="img" aria-label="Illustration of a checklist document with pen" style="background:linear-gradient(135deg,#e6e9ee,#8bc36a)"></div></div>
    <div class="service-label">CUSTOMS<br>CLEARANCE</div>
  </div>
  <div class="service" style="left:773px;top:1087px">
    <div class="service-tile"><div class="service-art" role="img" aria-label="Illustration of a delivery truck" style="background:linear-gradient(135deg,#4fa0e0,#f5c64a)"></div></div>
    <div class="service-label">TRUCKING</div>
  </div>

  <div class="footer-brand"></div>
  <div class="logo-name logo-name--footer">Halvern<br>Shipping</div>

  <section class="footer-info">
    <p class="cta">SIGH UP TO RECEIVE YOUR SUITE#</p>
    <p class="contact">
      <svg width="16" height="16" viewBox="0 0 16 16"><circle cx="8" cy="8" r="7" fill="none" stroke="#fff" stroke-width="2"/><path d="M1 8h14M8 1c3 3 3 11 0 14M8 1c-3 3-3 11 0 14" fill="none" stroke="#fff" stroke-width="1.5"/></svg>
      www.halvernshipping-bs.com
    </p>
    <p class="contact">
      <svg width="16" height="22" viewBox="0 0 16 22"><path d="M8 1a7 7 0 0 1 7 7c0 5-7 13-7 13S1 13 1 8a7 7 0 0 1 7-7z" fill="none" stroke="#fff" stroke-width="2.5"/><circle cx="8" cy="8" r="2.5" fill="#fff"/></svg>
      42 seagrape ave,nassau,Bahamas
    </p>
    <p class="phone">
      <svg width="22" height="36" viewBox="0 0 22 36"><path d="M16 4 C6 6 4 14 4 18 C4 22 6 30 16 32 L18 26 L12 24 C10 20 10 16 12 12 L18 10 Z" fill="#fff"/></svg>
      555-0192
    </p>
    <div class="social"><span class="social-dot"></span>@halvernship</div>
  </section>
  <div class="footer-strip"></div>
</main>
</body>
</html>
```